Dog Shampoo producer needs a bottle Sticker design

We need a Sticker design for our new Dog Shampoo product. The brand is "Velmo". This is for one of our product for smaller dogs with emphasis on no-tear and paraben-free formula. Photos of the bottle design are attached. Dimensions on the bottle drawings are in milimeters. Sticker shape and sizes should follow the shape and size of bottle. Bottle volume is 500ml.

The back sticker contains a space for barcode, ingredients (please put 7 to 8 ingredient list common for shampoo, we can update later), have this idea for benefit: formulated by people who care: paraben-free and no-tear formula for healthier and happier dogs, distributed by: PT. Velmo Indonesia

Target Market(s)

Young, sociable, and connected dog owners who often post photos of their activities with their dogs on social media.

Industry/Entity Type

Product

Font styles to use
Decorative

Colors

Designer to choose colors to be used in the design.

Requirements
Must have
• "no-tear" and "paraben-free" texts written on the label to show the product's unique selling point
Nice to have
• picture or drawing of a dog.

```html
<!DOCTYPE html>
<html lang="en">
<head>
<meta charset="utf-8">
<title>Velmo Doggy Shampoo – Front Label</title>
<link rel="stylesheet" href="https://fonts.googleapis.com/css2?family=Chewy&family=Sniglet:wght@400;800&display=swap">
<style>
  :root {
    --backdrop: #939598;
    --label-white: #ffffff;
    --lime: #8dc63f;
    --lime-soft: #c5e39b;
    --ink: #111111;
    --pink: #e6177c;
    --sunny: #ffc814;
  }
  * { margin: 0; padding: 0; box-sizing: border-box; }
  html, body { width: 1200px; height: 2727px; overflow: hidden; }
  body { background: var(--backdrop); position: relative; font-family: "Sniglet", sans-serif; color: var(--ink); }

  .label-shape { position: absolute; left: 0; top: 0; width: 1200px; height: 2727px; }

  .brand-name {
    position: absolute; left: 340px; width: 520px; top: 448px;
    text-align: center; font-family: "Sniglet", sans-serif; font-weight: 800;
    font-size: 148px; line-height: 1; color: var(--ink); white-space: nowrap;
  }

  .scene-illustration { position: absolute; left: 0; top: 0; width: 1200px; height: 2727px; pointer-events: none; }

  .product-title {
    position: absolute; left: 0; width: 1200px; top: 1655px;
    text-align: center; font-family: "Chewy", sans-serif; color: var(--lime);
    font-size: 165px; line-height: 158px; letter-spacing: 4px; white-space: nowrap;
  }

  .claims {
    position: absolute; left: 0; width: 1200px; top: 2190px;
    text-align: center; font-family: "Sniglet", sans-serif; font-weight: 400;
    font-size: 100px; line-height: 138px; white-space: nowrap;
  }

  .volume {
    position: absolute; left: 0; width: 1200px; top: 2492px;
    text-align: center; font-family: "Sniglet", sans-serif; font-size: 46px; line-height: 1;
  }
</style>
</head>
<body>

<svg class="label-shape" viewBox="0 0 1200 2727" xmlns="http://www.w3.org/2000/svg" aria-hidden="true">
  <path class="label-outline"
        d="M378 200 H822 Q882 200 882 260 V540 Q882 592 930 630 L1090 750 Q1136 786 1136 856 V2590 Q1136 2660 1066 2660 H134 Q64 2660 64 2590 V856 Q64 786 110 750 L270 630 Q318 592 318 540 V260 Q318 200 378 200 Z"
        fill="var(--label-white)" stroke="var(--lime)" stroke-width="30"/>
  <g class="bubbles">
    <circle cx="460" cy="280" r="20" fill="var(--lime)"/>
    <circle cx="590" cy="370" r="20" fill="var(--lime-soft)"/>
    <circle cx="722" cy="300" r="20" fill="var(--lime-soft)"/>
    <circle cx="765" cy="365" r="11" fill="var(--lime)"/>
    <circle cx="543" cy="382" r="11" fill="var(--lime)"/>
    <circle cx="222" cy="815" r="16" fill="var(--lime-soft)"/>
    <circle cx="236" cy="865" r="14" fill="var(--lime)"/>
    <circle cx="168" cy="868" r="10" fill="var(--lime)"/>
    <circle cx="173" cy="915" r="22" fill="var(--lime-soft)"/>
    <circle cx="910" cy="2500" r="16" fill="var(--lime-soft)"/>
    <circle cx="995" cy="2500" r="10" fill="var(--lime-soft)"/>
    <circle cx="935" cy="2545" r="18" fill="var(--lime)"/>
    <circle cx="1040" cy="2535" r="26" fill="var(--lime)"/>
  </g>
  <line x1="238" y1="2120" x2="545" y2="2120" stroke="var(--ink)" stroke-width="7" stroke-linecap="round"/>
  <line x1="655" y1="2120" x2="972" y2="2120" stroke="var(--ink)" stroke-width="7" stroke-linecap="round"/>
  <path d="M600 2156 C560 2128 552 2108 560 2094 C570 2078 592 2082 600 2098 C608 2082 630 2078 640 2094 C648 2108 640 2128 600 2156 Z"
        fill="var(--pink)" stroke="var(--ink)" stroke-width="6" stroke-linejoin="round"/>
</svg>

<div class="brand-name">Velmo</div>

<svg class="scene-illustration" viewBox="0 0 1200 2727" xmlns="http://www.w3.org/2000/svg" role="img"
     aria-label="Illustration: cartoon dog in a pink towel peeking through a yellow bathroom doorway, bubbly bathtub and green checkered floor">
  <defs>
    <linearGradient id="bathroomTones" x1="0" y1="0" x2="0" y2="1">
      <stop offset="0" stop-color="#ffd23f"/>
      <stop offset="0.62" stop-color="#f7e7a8"/>
      <stop offset="0.72" stop-color="#a9d46a"/>
      <stop offset="1" stop-color="#8dc63f"/>
    </linearGradient>
  </defs>
  <path d="M312 1598 V960 Q312 680 602 680 Q892 680 892 960 V1598 Z"
        fill="url(#bathroomTones)" stroke="var(--ink)" stroke-width="8"/>
  <line x1="238" y1="1600" x2="965" y2="1600" stroke="var(--ink)" stroke-width="9" stroke-linecap="round"/>
</svg>

<div class="product-title">DOGGY<br>SHAMPOO</div>

<div class="claims">No-Tear<br>Paraben-Free</div>

<div class="volume">500 ml</div>

</body>
</html>
```